Health & Beauty Company- Business Card Design

Two-sided business card design and logo design.

Company markets and sells otc treatments for the health and beauty industry. Marketing products to doctors, pharmacists and retail drug companies like tormundos, pqz and lumo fex.

Designs should be submitted as vector based PDFs. To keep your text in vector format, our printer recommends applications like Adobe Illustrator, Adobe InDesign and more recent versions of Adobe Photoshop.

Target Market(s)

Drug stores, doctors and pharmacists

Industry/Entity Type

Printer

Requirements
Must have
• Back side of business card should include company logo and our tagline: "Advancing Everyday Wellness & Care Solutions"

Company name acronym must be included: QTRM

```html
<!DOCTYPE html>
<html lang="en">
<head>
<meta charset="utf-8">
<title>QTRM Business Card – Front</title>
<link rel="stylesheet" href="https://fonts.googleapis.com/css2?family=Source+Sans+3:wght@400;600&display=swap">
<style>
  :root {
    --card-bg: #ffffff;
    --brand-black: #000000;
    --logo-grey: #c9c9c9;
    --name-grey: #6e6e6e;
    --title-teal: #1aa39a;
    --ink: #222222;
    --phone-grey: #6b6b6b;
    --fax-pink: #e0457b;
    --handle-blue: #2e5aa8;
    --photo-light: #eef3f4;
    --photo-teal: #7fc3c0;
    --photo-white: #f8f8f8;
  }
  html, body {
    margin: 0;
    padding: 0;
    overflow: hidden;
    background: var(--card-bg);
  }
  .card {
    position: relative;
    width: 1200px;
    height: 686px;
    background: var(--card-bg);
    font-family: "Source Sans 3", "Myriad Pro", Arial, sans-serif;
    overflow: hidden;
  }
  .logo-block {
    position: absolute;
    left: 0;
    top: 0;
    width: 378px;
    height: 261px;
    background: var(--brand-black);
  }
  .logo-block .mark {
    position: absolute;
    left: 80px;
    top: 102px;
    width: 36px;
    height: 36px;
    border-radius: 50%;
    background: var(--logo-grey);
  }
  .logo-block .brand-name {
    position: absolute;
    left: 132px;
    top: 96px;
    margin: 0;
    font-size: 42px;
    font-weight: 400;
    line-height: 1;
    color: var(--logo-grey);
    letter-spacing: 1px;
  }
  .logo-block .tagline {
    position: absolute;
    left: 74px;
    top: 152px;
    margin: 0;
    font-size: 10px;
    color: var(--logo-grey);
    letter-spacing: 0.2px;
    white-space: nowrap;
  }
  .holder-name {
    position: absolute;
    left: 466px;
    top: 14px;
    margin: 0;
    font-size: 40px;
    font-weight: 400;
    color: var(--name-grey);
  }
  .holder-title {
    position: absolute;
    left: 468px;
    top: 76px;
    margin: 0;
    font-size: 27px;
    font-weight: 400;
    color: var(--title-teal);
  }
  .team-photo {
    position: absolute;
    left: 92px;
    top: 300px;
    width: 570px;
    height: 362px;
    border-radius: 40% 40% 8% 8% / 30% 30% 6% 6%;
    background: linear-gradient(180deg, var(--photo-light) 0%, var(--photo-white) 35%, var(--photo-teal) 75%, var(--photo-light) 100%);
  }
  .address {
    position: absolute;
    left: 722px;
    top: 208px;
    margin: 0;
    font-style: normal;
    font-size: 40px;
    line-height: 51px;
    color: var(--ink);
  }
  .contact {
    position: absolute;
    left: 722px;
    margin: 0;
    font-size: 32px;
    line-height: 51px;
    color: var(--phone-grey);
    white-space: nowrap;
  }
  .contact.phones { top: 396px; }
  .contact.online { top: 530px; }
  .contact .label-fax { color: var(--fax-pink); }
  .contact .label-chat { color: var(--handle-blue); }
  .contact p { margin: 0; }
</style>
</head>
<body>
  <main class="card">
    <section class="logo-block" aria-label="QTRM logo">
      <span class="mark" aria-hidden="true"></span>
      <h1 class="brand-name">QTRM</h1>
      <p class="tagline">Advancing Everyday Wellness &amp; Care Solutions</p>
    </section>

    <h2 class="holder-name">Name xxxx</h2>
    <p class="holder-title">President &amp; CEO</p>

    <div class="team-photo" role="img" aria-label="Photograph of a group of doctors and nurses in white coats and scrubs"></div>

    <address class="address">
      Company<br>
      Address xxxx<br>
      city, State Zip code
    </address>

    <div class="contact phones">
      <p>xxx.xxx.xxx.</p>
      <p>xxx.xxx.xxx. <span class="label-fax">FAX</span></p>
    </div>

    <div class="contact online">
      <p>xxxx@xxxxxxxxxxxxx.com</p>
      <p>xxxxxx.xxxxxx <span class="label-chat">Voxly</span></p>
    </div>
  </main>
</body>
</html>
```